Vel

I have the logo for the back already. Need the front to match.
Need a VEL logo which I can provide or you can download one - VEL Realty in canada... Back of the card will be my logo and name. Front will have the info...
I would like a black background. Match colors on front to the back..
Details on Card

Target Market(s)

Realestate clients.. Keep it classy like the logo

Contact Information for Business Card

Reena Dhot office - 4035550187 cell - 4035550264 email - Reena@ReenaDhot.Com. website - ReenaDhot.Com Facebook - RDhotRealty Instagram - Reena_Yyc_Realtor Address - 514 - 23 St NE | T3K5M8

Colors
3176b5
33a6d7
85cae6

Requirements
Must have
• same color scheme as the logo
logo will be on the back
Black Background
Horizontal card
The one side of the card should be clean. like I stated, just my logo " Reena Dhot " and nothing else

```html
<!DOCTYPE html>
<html lang="en">
<head>
<meta charset="utf-8">
<title>Reena Dhot – Business Card</title>
<link href="https://fonts.googleapis.com/css2?family=Marcellus&family=Tinos&display=swap" rel="stylesheet">
<style>
  :root {
    --stage: #1c1c1d;
    --card: #201f20;
    --card-edge: #2a292a;
    --text: #f2f2f2;
    --silver: #d9dadc;
    --blue-deep: #3176b5;
    --blue: #33a6d7;
    --blue-light: #85cae6;
    --rule: #d8d8d8;
  }
  * { box-sizing: border-box; margin: 0; padding: 0; }
  html, body { width: 1200px; height: 1200px; overflow: hidden; background: var(--stage); }
  .canvas { position: relative; width: 1200px; height: 1200px; }

  .card {
    position: absolute;
    left: 180px;
    width: 840px;
    height: 480px;
    background: var(--card);
    border: 1px solid var(--card-edge);
  }
  .card--info { top: 90px; }
  .card--brand { top: 630px; display: flex; align-items: center; justify-content: center; }

  .contact-list { position: absolute; left: 62px; list-style: none; font-family: "Tinos", serif; color: var(--text); font-size: 19px; }
  .contact-list li { display: flex; align-items: center; gap: 14px; height: 27px; white-space: nowrap; }
  .contact-list svg { width: 16px; height: 16px; flex: none; }
  .contact-list--top { top: 50px; }
  .contact-list--bottom { top: 270px; }

  .social-dot { width: 14px; height: 14px; border-radius: 50%; background: var(--blue); flex: none; margin: 0 1px; }

  .name-mark { position: absolute; right: 70px; top: 140px; text-align: right; }
  .name-mark__text { font-family: "Marcellus", serif; font-size: 34px; letter-spacing: 3px; color: var(--text); text-transform: uppercase; }
  .name-mark__rule { height: 3px; width: 100px; background: var(--blue); margin-left: auto; margin-top: 4px; }

  .divider { position: absolute; left: 100px; right: 70px; top: 245px; height: 1px; background: var(--rule); }

  .affiliations { position: absolute; right: 70px; bottom: 44px; display: flex; align-items: center; gap: 28px; }
  .badge { border: 2px solid var(--silver); opacity: .8; }
  .badge--network { width: 88px; height: 60px; border-radius: 4px; }
  .badge--luxury { width: 122px; height: 54px; }
  .brokerage { font-family: "Marcellus", serif; font-size: 21px; color: var(--silver); letter-spacing: 1px; text-transform: uppercase; white-space: nowrap; }

  .brand-name { font-family: "Marcellus", serif; font-size: 84px; letter-spacing: 6px; color: var(--silver); text-transform: uppercase; }
</style>
</head>
<body>
<main class="canvas">
  <section class="card card--info" aria-label="Card front with contact details">
    <ul class="contact-list contact-list--top">
      <li>
        <svg viewBox="0 0 16 16"><path fill="#33a6d7" d="M3 1h3l1.5 4-2 1.2a9 9 0 0 0 4.3 4.3L11 8.5l4 1.5v3a2 2 0 0 1-2 2A12 12 0 0 1 1 3a2 2 0 0 1 2-2z"/></svg>
        4035550187
      </li>
      <li>
        <svg viewBox="0 0 16 16"><rect x="4" y="1" width="8" height="14" rx="1.5" fill="none" stroke="#33a6d7" stroke-width="1.6"/><circle cx="8" cy="12.5" r="0.9" fill="#33a6d7"/></svg>
        4035550264
      </li>
      <li>
        <svg viewBox="0 0 16 16"><rect x="1" y="3" width="14" height="10" fill="#33a6d7"/><path d="M1 3l7 6 7-6" fill="none" stroke="#201f20" stroke-width="1.3"/></svg>
        Reena@ReenaDhot.Com.
      </li>
      <li>
        <svg viewBox="0 0 16 16"><g fill="none" stroke="#33a6d7" stroke-width="1.3"><circle cx="8" cy="8" r="6.5"/><ellipse cx="8" cy="8" rx="3" ry="6.5"/><path d="M1.5 8h13M2.5 5h11M2.5 11h11"/></g></svg>
        www.ReenaDhot.Com
      </li>
    </ul>

    <div class="name-mark">
      <div class="name-mark__text">Reena Dhot</div>
      <div class="name-mark__rule"></div>
    </div>

    <div class="divider"></div>

    <ul class="contact-list contact-list--bottom">
      <li><span class="social-dot"></span>RDhotRealty</li>
      <li><span class="social-dot"></span>Reena_Yyc_Realtor</li>
      <li>
        <svg viewBox="0 0 16 16"><path fill="#33a6d7" d="M8 1a5 5 0 0 1 5 5c0 4-5 9-5 9S3 10 3 6a5 5 0 0 1 5-5z"/><circle cx="8" cy="6" r="1.8" fill="#201f20"/></svg>
        514 - 23 St NE | T3K5M8
      </li>
    </ul>

    <div class="affiliations">
      <div class="badge badge--network" role="img" aria-label="Partner network badge"></div>
      <div class="brokerage">VEL Realty</div>
      <div class="badge badge--luxury" role="img" aria-label="Luxury listing program badge"></div>
    </div>
  </section>

  <section class="card card--brand" aria-label="Card back with name">
    <div class="brand-name">Reena Dhot</div>
  </section>
</main>
</body>
</html>
```